Webdesign für  Kranken- und Seniorenpflege
Webdesign für Kranken- und Seniorenpflege
Zielgruppe
Ambulante Kranken- und Seniorenpflege
Tagespflege in Kirchwald-Steinau, Auenried und Talbrunn
Palliativpflege
Aufgabenstellung
- Erstellung in Adobe Photoshop
- Orientieren Sie sich am Socialmedia-Auftritt des Kunden

```html
<!DOCTYPE html>
<html lang="de">
<head>
<meta charset="utf-8">
<title>Pflegenah Sachsen – Ambulante Kranken- und Seniorenpflege</title>
<link href="https://fonts.googleapis.com/css2?family=Fira+Sans+Condensed:ital,wght@0,400;0,500;0,600;1,500;1,600;1,700&display=swap" rel="stylesheet">
<style>
  :root{
    --yellow:#f4c316;
    --yellow-deep:#eab308;
    --crimson:#a80a45;
    --white:#ffffff;
    --paper:#f6f5f3;
    --ink:#3a3a3a;
  }
  *{box-sizing:border-box;margin:0;padding:0}
  html,body{width:1200px;height:794px;overflow:hidden;background:var(--paper)}
  body{font-family:"Fira Sans Condensed",sans-serif;color:var(--ink)}
  .page{position:relative;width:1200px;height:794px;background:var(--white);overflow:hidden}

  /* header */
  .header{position:absolute;inset:0 0 auto 0;height:170px}
  .header-wave{position:absolute;top:0;right:0;width:720px;height:126px}
  .brand{position:absolute;left:48px;top:28px;display:flex;align-items:center;gap:10px}
  .brand-dot{width:44px;height:44px;border-radius:50%;background:var(--yellow)}
  .brand-name{font-weight:600;font-size:20px;color:var(--crimson)}
  .tagline{position:absolute;left:48px;top:86px;font-style:italic;font-weight:600;font-size:28px;color:var(--yellow)}
  .nav{position:absolute;left:48px;top:136px;display:flex;font-size:14px;color:#444}
  .nav a{color:inherit;text-decoration:none;padding:0 10px;border-left:1px solid #777}
  .nav a:first-child{padding-left:0;border-left:0}
  .contact{position:absolute;right:60px;top:14px;text-align:right;color:var(--crimson)}
  .legal{font-size:11px;color:var(--white)}
  .mail{margin-top:4px;font-size:14px;color:var(--white);display:flex;align-items:center;justify-content:flex-end;gap:6px}
  .hotline{margin-top:8px;display:flex;align-items:center;justify-content:flex-end;gap:12px}
  .hotline-icon{width:46px;height:46px;border-radius:50%;background:var(--crimson);display:grid;place-items:center}
  .hotline-text small{display:block;font-size:13px;font-weight:500;color:#3a2a00;text-align:left}
  .hotline-text strong{font-style:italic;font-weight:700;font-size:34px;line-height:1}
  .social{position:absolute;right:60px;top:136px;display:flex;gap:8px}
  .social span{width:16px;height:16px;border-radius:50%;background:var(--crimson)}

  /* hero */
  .hero{position:absolute;left:0;top:170px;width:1200px;height:370px;overflow:hidden}
  .hero-photo{position:absolute;inset:0;background:linear-gradient(110deg,#e9e4dc 0%,#d9cbb8 30%,#c79a86 48%,#8c2a3c 60%,#e8ddd0 78%,#cfa53a 100%)}
  .hero-band{position:absolute;left:0;bottom:0;width:1200px;height:220px}
  .hero-title{position:absolute;left:60px;bottom:46px;font-style:italic;font-weight:600;font-size:36px;line-height:1.15;color:var(--white)}
  .hero-arrow{position:absolute;top:150px;width:34px;height:34px;border-radius:50%;background:rgba(255,255,255,.85);display:grid;place-items:center}
  .hero-arrow.prev{left:24px}.hero-arrow.next{right:24px}

  /* locations */
  .locations{position:absolute;left:0;top:540px;width:1200px;height:136px;padding:14px 60px 0}
  .section-kicker{font-style:italic;font-weight:600;font-size:18px;color:var(--crimson)}
  .location-grid{display:grid;grid-template-columns:repeat(3,1fr);gap:4px 40px;margin-top:8px}
  .location{display:flex;align-items:center;gap:8px;font-style:italic;font-weight:600;font-size:22px;color:var(--yellow-deep)}
  .location small{font-size:13px;color:var(--crimson);margin-right:4px}
  .pin{flex:none;width:14px;height:14px;border-radius:50%;border:4px solid var(--crimson);background:var(--white)}
  .headquarters{grid-column:2;display:flex;align-items:center;gap:6px;font-size:12px;color:#333;border-top:2px solid var(--yellow);width:200px;padding-top:3px}

  /* advice */
  .advice{position:absolute;left:0;top:676px;width:1200px;height:118px;display:flex;gap:40px;padding:0 60px}
  .advice-photo{width:320px;height:118px;border-radius:14px 14px 0 0;background:linear-gradient(135deg,#cfcac4,#8d8a86 55%,#3f4a5e)}
  .advice-body{padding-top:4px;width:560px}
  .advice-title{font-style:italic;font-weight:600;font-size:28px;line-height:1.1;color:var(--crimson)}
  .advice-text{font-size:14px;line-height:1.35;margin-top:4px}
  .advice-links{list-style:none;display:flex;gap:22px;margin-top:8px}
  .advice-links li{display:flex;align-items:center;gap:6px;font-style:italic;font-weight:600;font-size:13px;color:var(--crimson)}
  .chev{width:16px;height:16px;border-radius:50%;background:var(--yellow);display:grid;place-items:center}
</style>
</head>
<body>
<div class="page">
  <header class="header">
    <svg class="header-wave" viewBox="0 0 720 126" preserveAspectRatio="none" aria-hidden="true">
      <path d="M40 0 H720 V50 C600 110 400 126 120 126 C260 100 300 50 40 0 Z" fill="#f4c316"/>
    </svg>
    <div class="brand"><span class="brand-dot"></span><span class="brand-name">Pflegenah Sachsen</span></div>
    <div class="tagline">Ambulante Kranken- und Seniorenpflege</div>
    <nav class="nav">
      <a href="#">Kranken- und Seniorenpflege</a><a href="#">Tagespflege</a><a href="#">Palliativpflege</a><a href="#">Pflegeberatung</a><a href="#">Standorte</a><a href="#">Stellenangebote</a><a href="#">Aktuelles</a>
    </nav>
    <div class="contact">
      <div class="legal">Impressum | Datenschutz</div>
      <div class="mail">
        <svg width="14" height="10" viewBox="0 0 14 10" aria-hidden="true"><rect x="0.5" y="0.5" width="13" height="9" fill="none" stroke="#fff"/><path d="M1 1 L7 6 L13 1" fill="none" stroke="#fff"/></svg>
        info@pflegenah-sachsen.de
      </div>
      <div class="hotline">
        <span class="hotline-icon">
          <svg width="24" height="24" viewBox="0 0 24 24" aria-hidden="true"><path d="M4 9 C4 5 20 5 20 9 L17 11 L15 9 H9 L7 11 Z M7 13 H17 V18 H7 Z" fill="none" stroke="#fff" stroke-width="1.6" stroke-linejoin="round"/></svg>
        </span>
        <span class="hotline-text"><small>Wir sind jederzeit kostenfrei für Sie da.</small><strong>0800 5270318</strong></span>
      </div>
    </div>
    <div class="social"><span></span><span></span></div>
  </header>

  <section class="hero">
    <div class="hero-photo" role="img" aria-label="Pflegerin mit Strickmütze lacht herzlich mit einer älteren Dame"></div>
    <svg class="hero-band" viewBox="0 0 1200 220" preserveAspectRatio="none" aria-hidden="true">
      <path d="M0 220 V110 C180 40 520 20 860 60 C980 74 1100 70 1200 40 V220 Z" fill="#f4c316" opacity=".92"/>
      <path d="M860 220 C960 160 1100 130 1200 120 V220 Z" fill="#ffffff"/>
    </svg>
    <h1 class="hero-title">Weil wir für das brennen,<br>was wir tun – Pflegenah Sachsen!</h1>
    <span class="hero-arrow prev"><svg width="12" height="12" viewBox="0 0 12 12" aria-hidden="true"><path d="M8 1 L3 6 L8 11" fill="none" stroke="#a80a45" stroke-width="2"/></svg></span>
    <span class="hero-arrow next"><svg width="12" height="12" viewBox="0 0 12 12" aria-hidden="true"><path d="M4 1 L9 6 L4 11" fill="none" stroke="#a80a45" stroke-width="2"/></svg></span>
  </section>

  <section class="locations">
    <h2 class="section-kicker">Unsere Standorte</h2>
    <div class="location-grid">
      <div class="location"><span class="pin"></span>Talbrunn</div>
      <div class="location"><span class="pin"></span>Kirchwald-Steinau</div>
      <div class="location"><span class="pin"></span>Auenried</div>
      <div class="location"><span class="pin"></span><small>Tagespflege</small>Talbrunn</div>
      <div class="location"><span class="pin"></span><small>Tagespflege</small>Kirchwald-Steinau</div>
      <div class="location"><span class="pin"></span><small>Tagespflege</small>Auenried</div>
      <div class="headquarters">
        <svg width="12" height="11" viewBox="0 0 12 11" aria-hidden="true"><path d="M1 5 L6 1 L11 5 V10 H1 Z" fill="#f4c316"/></svg>
        Firmensitz und Verwaltung
      </div>
    </div>
  </section>

  <section class="advice">
    <div class="advice-photo" role="img" aria-label="Älterer Herr im Gespräch bei der Pflegeberatung"></div>
    <div class="advice-body">
      <h2 class="advice-title">Pflegeberatung</h2>
      <p class="advice-text">In diesem Bereich erhalten Sie aktuelle Informationen – die Ihnen helfen die Pflege und Betreuung Ihrer Angehörigen weiter zu verbessern.</p>
      <ul class="advice-links">
        <li><span class="chev"><svg width="8" height="8" viewBox="0 0 8 8" aria-hidden="true"><path d="M2 1 L6 4 L2 7" fill="none" stroke="#a80a45" stroke-width="1.5"/></svg></span>Beratung, Hilfe bei Anträgen</li>
        <li><span class="chev"><svg width="8" height="8" viewBox="0 0 8 8" aria-hidden="true"><path d="M2 1 L6 4 L2 7" fill="none" stroke="#a80a45" stroke-width="1.5"/></svg></span>Pflege-Info</li>
        <li><span class="chev"><svg width="8" height="8" viewBox="0 0 8 8" aria-hidden="true"><path d="M2 1 L6 4 L2 7" fill="none" stroke="#a80a45" stroke-width="1.5"/></svg></span>Pflegekurse</li>
      </ul>
    </div>
  </section>
</div>
</body>
</html>
```